Packaging Design Project

I need a box for a hair oil called KEZ. 3 color, Simple design .. We are open to new ideas, the over all theme.. Pure and Simple , Natural, Color protect, good for the hair. We started with a basic design and this is the existing website http://kezhaircare.com/

Hair

```html
<!DOCTYPE html>
<html lang="en">
<head>
<meta charset="utf-8">
<title>KEZ Hair Care – Box Front</title>
<link rel="stylesheet" href="https://fonts.googleapis.com/css2?family=Raleway:wght@300&family=Patrick+Hand&display=swap">
<style>
  :root {
    --page-bg: #ffffff;
    --panel-brown: #4a2818;
    --panel-pattern: #552e1c;
    --brand-green: #3fc62c;
    --soft-green: #3aa82e;
    --rust: #a9593b;
  }
  html, body {
    margin: 0;
    padding: 0;
    width: 965px;
    height: 1200px;
    overflow: hidden;
    background: var(--page-bg);
  }
  .canvas {
    position: relative;
    width: 965px;
    height: 1200px;
  }
  .box-front {
    position: absolute;
    left: 252px;
    top: 35px;
    width: 460px;
    height: 1130px;
    background: var(--panel-brown);
    font-family: "Raleway", sans-serif;
    font-weight: 300;
    text-align: center;
    overflow: hidden;
  }
  .leaf-pattern {
    position: absolute;
    inset: 0;
    width: 100%;
    height: 100%;
  }
  .brand-name {
    position: absolute;
    left: 0;
    right: 0;
    top: 268px;
    margin: 0;
    font-family: "Raleway", sans-serif;
    font-weight: 300;
    font-size: 118px;
    line-height: 1;
    letter-spacing: 6px;
    color: var(--brand-green);
  }
  .brand-line {
    position: absolute;
    left: 0;
    right: 0;
    top: 398px;
    margin: 0;
    font-size: 31px;
    line-height: 1;
    color: var(--soft-green);
  }
  .product-title {
    position: absolute;
    left: 0;
    right: 0;
    top: 462px;
    margin: 0;
    font-size: 31px;
    line-height: 41px;
    font-weight: 300;
    color: var(--soft-green);
  }
  .claims {
    position: absolute;
    left: 0;
    right: 0;
    top: 647px;
    margin: 0;
    padding: 0;
    list-style: none;
    font-size: 29px;
    line-height: 35px;
    color: var(--rust);
  }
  .benefits {
    position: absolute;
    left: 30px;
    right: 30px;
    top: 887px;
    margin: 0;
    font-family: "Patrick Hand", cursive;
    font-size: 29px;
    line-height: 35px;
    color: var(--brand-green);
  }
  .volume {
    position: absolute;
    left: 0;
    right: 0;
    top: 1060px;
    margin: 0;
    font-size: 28px;
    line-height: 1;
    color: var(--soft-green);
  }
</style>
</head>
<body>
  <main class="canvas">
    <section class="box-front">
      <svg class="leaf-pattern" role="img" aria-label="Faint decorative pattern of leaves, vines and berries across the brown panel" viewBox="0 0 460 1130" preserveAspectRatio="none">
        <rect width="460" height="1130" fill="var(--panel-pattern)" opacity="0.35"/>
      </svg>

      <h1 class="brand-name">KEZ</h1>
      <p class="brand-line">hair care</p>

      <h2 class="product-title">Protective hair- oil<br>treatment<br>and styling aid</h2>

      <ul class="claims">
        <li>paraben free</li>
        <li>sulfate free</li>
        <li>alergy tested</li>
        <li>alcohol free</li>
      </ul>

      <p class="benefits">style, smooth, shine &amp; condition ALL hair of types while looking in moisture</p>

      <p class="volume">100 ml/ 3.4 oz</p>
    </section>
  </main>
</body>
</html>
```